Lantern Keepers Lantern Scribes

We would like the business card to be Horizontal
Logo on the back and want it raised.

Target Market(s)

Education and Museums

Industry/Entity Type

Education

Contact Information for Business Card

Joanne Valdoro, P.H.D.
2918 Pemberly Rd
Laurel, MD 20914
612.447.3091
Joanne.Valdoro@lanternkeeperslanternscribes.org
lanternkeeperslanternscribes.org

Font styles to use
Serif

Colors

Designer to choose colors to be used in the design.

Requirements
Must have
• letters and logo must be raised
• Must be slate blue card
• Silver is aluminum foil

```html
<!DOCTYPE html>
<html lang="en">
<head>
<meta charset="utf-8">
<title>Lantern Keepers Lantern Scribes – Business Card</title>
<link href="https://fonts.googleapis.com/css2?family=Libre+Baskerville:wght@400;700&display=swap" rel="stylesheet">
<style>
  :root {
    --backdrop: #2f3236;
    --card: #4a5a78;
    --card-deep: #3d4b66;
    --foil: #dfe3e8;
    --foil-soft: #c3c9d2;
    --rule: #9aa5b6;
    --icon-ink: #4a5a78;
  }
  * { margin: 0; padding: 0; box-sizing: border-box; }
  html, body {
    width: 1200px; height: 1108px; overflow: hidden;
    background: var(--backdrop);
    font-family: "Libre Baskerville", Georgia, serif;
  }
  .stage {
    width: 1200px; height: 1108px;
    display: flex; flex-direction: column; justify-content: center; align-items: center; gap: 60px;
  }
  .card {
    width: 760px; height: 434px;
    background: var(--card);
    border-radius: 22px;
    position: relative;
    color: var(--foil);
    overflow: hidden;
  }

  /* front */
  .card-front { display: flex; align-items: stretch; }
  .front-brand {
    width: 290px; display: flex; flex-direction: column; align-items: center; justify-content: center; gap: 20px;
    padding: 0 24px;
  }
  .brand-ring { width: 130px; height: 130px; border: 4px solid var(--foil); border-radius: 50%; }
  .brand-name {
    font-weight: 700; font-size: 17px; letter-spacing: 1.5px; text-transform: uppercase;
    text-align: center; line-height: 1.5;
  }
  .front-divider { width: 1px; background: var(--rule); margin: 50px 0; }
  .front-details {
    flex: 1; padding: 0 30px 0 36px;
    display: flex; flex-direction: column; justify-content: center;
  }
  .person-name { font-weight: 700; font-size: 24px; letter-spacing: 1px; text-transform: uppercase; }
  .person-title { font-size: 14px; color: var(--foil-soft); margin-top: 6px; }
  .icon-row { margin-top: 18px; display: flex; align-items: center; gap: 8px; }
  .icon-row .rule { flex: 1; height: 1px; background: var(--rule); }
  .icon {
    width: 22px; height: 22px; background: var(--foil); border-radius: 4px;
    display: flex; align-items: center; justify-content: center;
  }
  .contact { margin-top: 14px; font-size: 13px; line-height: 1.75; }
  .divider { height: 1px; background: var(--rule); margin: 12px 0; }
  .address { font-size: 13px; line-height: 1.75; }

  /* back */
  .back-pattern {
    position: absolute; inset: 0;
    background: linear-gradient(150deg, var(--card) 0%, var(--card-deep) 100%);
  }
  .back-mark {
    position: absolute; left: 0; right: 0; top: 150px;
    display: flex; flex-direction: column; align-items: center; gap: 16px;
  }
  .back-mark .brand-ring { width: 60px; height: 60px; border-width: 3px; }
  .back-mark .brand-name { font-size: 15px; letter-spacing: 2px; }
  .back-url {
    position: absolute; left: 0; right: 0; bottom: 44px;
    text-align: center; font-size: 14px; letter-spacing: 0.5px;
  }
</style>
</head>
<body>
<main class="stage">
  <section class="card card-front">
    <div class="front-brand">
      <div class="brand-ring"></div>
      <div class="brand-name">Lantern Keepers<br>Lantern Scribes</div>
    </div>
    <div class="front-divider"></div>
    <div class="front-details">
      <div class="person-name">Joanne Valdoro</div>
      <div class="person-title">Managing Director</div>
      <div class="icon-row">
        <span class="icon"><svg width="14" height="14" viewBox="0 0 16 16"><path d="M3 2h3l1 3-2 1a8 8 0 0 0 5 5l1-2 3 1v3c0 1-1 1-1 1A12 12 0 0 1 2 3s0-1 1-1z" fill="#4a5a78"/></svg></span>
        <span class="icon"><svg width="14" height="14" viewBox="0 0 16 16"><rect x="2" y="4" width="12" height="8" fill="none" stroke="#4a5a78" stroke-width="1.6"/><path d="M2 4l6 5 6-5" fill="none" stroke="#4a5a78" stroke-width="1.6"/></svg></span>
        <span class="icon"><svg width="14" height="14" viewBox="0 0 16 16"><circle cx="8" cy="8" r="6" fill="none" stroke="#4a5a78" stroke-width="1.6"/><path d="M2 8h12M8 2c-3 3-3 9 0 12M8 2c3 3 3 9 0 12" fill="none" stroke="#4a5a78" stroke-width="1.2"/></svg></span>
        <span class="rule"></span>
      </div>
      <div class="contact">
        612.447.3091<br>
        Joanne.Valdoro@lanternkeeperslanternscribes.org<br>
        lanternkeeperslanternscribes.org
      </div>
      <div class="divider"></div>
      <div class="address">2918 Pemberly Rd,<br>Laurel, MD 20914</div>
    </div>
  </section>

  <section class="card card-back">
    <div class="back-pattern" role="img" aria-label="Faint repeating brand pattern across the card back"></div>
    <div class="back-mark">
      <div class="brand-ring"></div>
      <div class="brand-name">Lantern Keepers Lantern Scribes</div>
    </div>
    <div class="back-url">lanternkeeperslanternscribes.org</div>
  </section>
</main>
</body>
</html>
```